Author needs a new book, Kindle and Audiobook cover design

I updated and re-edited a book I wrote 25 years ago but now realize the title and design did not get the job done. I am seeking a book, Kindle and audiobook design that will make me stand out. The final design will pop while being sensitive to the nature of the subject. The title of the book is Quiet Lanterns. Subtitle: Ways to Notice and Step Away From Harmful Circles While Keeping Steady Belief by Dorian T. Wexcombe. I am wanting to get the attention of people who have been damaged by a church relationship that started well but ended badly.
Updates

The book title is: Quiet Lanterns. The Subtitle is: Ways To Notice and Step Away From Harmful Circles While Keeping Steady Belief. The dimension is 6x9 (150 pages) and I am the author: Dorian T. Wexcombe

Target Market(s)

People with a church experience; church leadership. Religious abuse victims.

Industry/Entity Type

Christian

Font styles to use
Serif

Colors

Designer to choose colors to be used in the design.

Requirements
Nice to have
• I am not married to the Serif font if another design works better.

```html
<!DOCTYPE html>
<html lang="en">
<head>
<meta charset="utf-8">
<title>Quiet Lanterns — Book Cover</title>
<link rel="stylesheet" href="https://fonts.googleapis.com/css2?family=Montserrat:wght@300;400;700&family=Cinzel:wght@400&display=swap">
<style>
  :root {
    --stage: #e6e7e9;
    --cover: #f3f3f4;
    --ink: #1f2a44;
    --ink-soft: #2b3550;
    --sky: #3aa3dc;
    --mist: #d5d9de;
    --ember: #f0a945;
  }
  * { margin: 0; padding: 0; box-sizing: border-box; }
  html, body {
    width: 1200px;
    height: 928px;
    overflow: hidden;
    background: var(--stage);
  }
  .canvas {
    position: relative;
    width: 1200px;
    height: 928px;
    display: flex;
    align-items: center;
    justify-content: center;
  }
  .cover {
    position: relative;
    width: 574px;
    height: 860px;
    background: var(--cover);
    box-shadow: 0 2px 10px rgba(0,0,0,0.08);
    display: flex;
    flex-direction: column;
    align-items: center;
    text-align: center;
    color: var(--ink);
  }
  .cover-title {
    margin-top: 58px;
    font-family: "Montserrat", sans-serif;
    font-weight: 700;
    font-size: 58px;
    line-height: 1.05;
    letter-spacing: 0.2em;
    text-transform: uppercase;
    padding-left: 0.2em;
  }
  .cover-subtitle {
    margin-top: 24px;
    font-family: "Montserrat", sans-serif;
    font-weight: 400;
    font-size: 18px;
    line-height: 1.2;
    letter-spacing: 0.04em;
    text-transform: uppercase;
    color: var(--ink-soft);
  }
  .cover-subtitle span {
    display: block;
    white-space: nowrap;
  }
  .cover-artwork {
    margin-top: 58px;
    width: 400px;
    height: 250px;
    border-radius: 6px;
    background: linear-gradient(180deg, var(--sky) 0%, var(--mist) 52%, var(--ember) 100%);
    opacity: 0.85;
  }
  .cover-author {
    margin-top: auto;
    margin-bottom: 78px;
    font-family: "Cinzel", serif;
    font-weight: 400;
    font-size: 31px;
    letter-spacing: 0.06em;
    color: var(--ink);
  }
</style>
</head>
<body>
<main class="canvas">
  <section class="cover">
    <h1 class="cover-title">Quiet<br>Lanterns</h1>
    <p class="cover-subtitle">
      <span>Ways to Notice and Step Away</span>
      <span>From Harmful Circles</span>
      <span>While Keeping Steady Belief</span>
    </p>
    <div class="cover-artwork" role="img" aria-label="Cover artwork: light recessed window shape with sky blue above and warm amber glow below"></div>
    <p class="cover-author">Dorian T. Wexcombe</p>
  </section>
</main>
</body>
</html>
```